Tech Company Letterhead/Business Cards/Envelopes

We would like a new stationary design for a technology company that develops full turnkey solutions for governments related to Data, Identity Tracking, Fingerprinting, Passport Control, and Border Protection Systems.

We would like the stationary designs to include:

Letter Head
Business Cards
Envelopes

Target Market(s)

Corporate

Industry/Entity Type

Business

Contact Information for Business Card

Details to be shared with the winner.

Font styles to use
Serif
Sans Serif

Colors
e4daeb
85abd2
3176b5
0355a3
0692cd

```html
<!DOCTYPE html>
<html lang="en">
<head>
<meta charset="utf-8">
<title>Norvix Stationery</title>
<link rel="stylesheet" href="https://fonts.googleapis.com/css2?family=Open+Sans:ital,wght@0,400;0,600;0,700;1,600;1,700&family=Tinos&display=swap">
<style>
  :root {
    --brand-blue: #0b72c1;
    --brand-deep: #0355a3;
    --brand-sky: #0692cd;
    --brand-ink: #1d4f8a;
    --band-grey: #55585e;
    --text-grey: #6a6d72;
    --paper: #ffffff;
    --backdrop: #e7eaec;
  }
  * { margin: 0; padding: 0; box-sizing: border-box; }
  html, body { width: 843px; height: 1200px; overflow: hidden; }
  body {
    background: var(--backdrop);
    font-family: "Open Sans", sans-serif;
    position: relative;
  }
  .piece {
    position: absolute;
    background: var(--paper);
    box-shadow: 0 2px 8px rgba(0,0,0,.12);
    overflow: hidden;
  }
  .wordmark {
    position: absolute;
    font-family: "Open Sans", sans-serif;
    font-weight: 700;
    color: var(--brand-blue);
    letter-spacing: .04em;
    line-height: 1;
  }
  .wordmark--tone { color: var(--brand-ink); }
  .footer-bands {
    position: absolute;
    left: 0; bottom: 0;
    width: 100%;
  }
  .footer-bands svg { display: block; width: 100%; height: 100%; }
  .footer-bands .wordmark { bottom: 22%; right: 8%; }
  .top-rule { position: absolute; top: 0; left: 0; right: 0; height: 4px; background: var(--brand-blue); }

  /* Envelope back */
  .envelope-back { left: 40px; top: 40px; width: 360px; height: 180px; }
  .envelope-back .flap { position: absolute; top: 0; left: 0; width: 100%; height: 44px; background: var(--brand-blue); }
  .envelope-back .flap .wordmark { color: var(--brand-ink); font-size: 16px; left: 50%; top: 14px; transform: translateX(-50%); }
  .envelope-back svg.fold { position: absolute; top: 44px; left: 0; width: 100%; height: 40px; }

  /* Small cards */
  .card-small-back { left: 40px; top: 240px; width: 170px; height: 100px; background: var(--brand-blue); }
  .card-small-back .wordmark { color: var(--brand-ink); font-size: 24px; left: 50%; top: 50%; transform: translate(-50%,-50%); }
  .card-small-front { left: 230px; top: 240px; width: 170px; height: 100px; }
  .card-small-front .wordmark { font-size: 11px; right: 10px; top: 12px; }
  .card-small-front .mini-details { position: absolute; left: 10px; top: 30px; font-size: 5.5px; line-height: 1.5; color: var(--text-grey); }
  .card-small-front .mini-details b { color: var(--brand-blue); font-style: italic; }
  .card-small-front .footer-bands { height: 20px; }
  .card-small-front .footer-bands .wordmark { font-size: 6px; }

  /* Envelope front */
  .envelope-front { left: 40px; top: 360px; width: 360px; height: 200px; }
  .envelope-front > .wordmark { font-size: 22px; left: 20px; top: 24px; }
  .envelope-front .return-address { position: absolute; left: 20px; bottom: 48px; font-size: 7px; line-height: 1.4; color: var(--text-grey); font-style: italic; }
  .envelope-front .footer-bands { height: 36px; }
  .envelope-front .footer-bands .wordmark { font-size: 11px; }

  /* Letterhead */
  .letterhead { left: 423px; top: 40px; width: 380px; height: 537px; }
  .letterhead > .wordmark { font-size: 22px; left: 26px; top: 22px; }
  .letterhead .header-contact { position: absolute; right: 24px; top: 18px; font-size: 6.5px; line-height: 1.45; color: var(--text-grey); }
  .letterhead .header-contact b { color: var(--brand-blue); }
  .letterhead .header-rule { position: absolute; left: 26px; right: 24px; top: 62px; height: 1px; background: var(--brand-blue); opacity: .4; }
  .letter-body {
    position: absolute; left: 26px; right: 30px; top: 80px;
    font-family: "Tinos", serif; font-size: 9px; line-height: 1.45; color: #222;
  }
  .letter-body p { margin-bottom: 8px; }
  .letterhead .footer-bands { height: 40px; }
  .letterhead .footer-bands .wordmark { font-size: 12px; }

  /* Large cards */
  .card-back { left: 303px; top: 600px; width: 500px; height: 286px; background: linear-gradient(135deg, var(--brand-sky), var(--brand-blue)); }
  .card-back .wordmark { color: var(--brand-ink); font-size: 78px; left: 50%; top: 50%; transform: translate(-50%,-50%); }

  .card-front { left: 40px; top: 860px; width: 560px; height: 320px; box-shadow: 0 6px 18px rgba(0,0,0,.18); }
  .card-front > .wordmark { font-size: 34px; right: 38px; top: 42px; }
  .card-front .holder { position: absolute; left: 40px; top: 78px; }
  .card-front .holder-name { font-size: 20px; font-weight: 700; font-style: italic; color: var(--brand-blue); }
  .card-front .holder-role { font-size: 14px; color: var(--text-grey); margin-left: 28px; margin-top: -4px; }
  .card-front .contact-list { position: absolute; left: 36px; top: 158px; list-style: none; font-size: 14px; line-height: 1.55; color: #4a4d52; }
  .card-front .contact-list b { color: var(--brand-blue); font-style: italic; font-weight: 700; }
  .card-front .footer-bands { height: 64px; }
  .card-front .footer-bands .wordmark { font-size: 20px; }
</style>
</head>
<body>

<section class="piece envelope-back" aria-label="Envelope back">
  <div class="flap"><span class="wordmark">NORVIX</span></div>
  <svg class="fold" viewBox="0 0 100 20" preserveAspectRatio="none"><polygon points="0,0 100,0 50,20" fill="#eceef0"/></svg>
</section>

<section class="piece card-small-back" aria-label="Business card back">
  <span class="wordmark">NORVIX</span>
</section>

<section class="piece card-small-front" aria-label="Business card front">
  <span class="wordmark">NORVIX</span>
  <div class="mini-details">
    <b>Daniel Harrow</b><br>Manager<br>
    <b>Address :</b> 22 PO Box 87, Lindale, Ohio 4512<br>
    <b>Email :</b> info@norvix.com<br>
    <b>Tel :</b> 1300 262 818
  </div>
  <div class="footer-bands">
    <svg viewBox="0 0 100 20" preserveAspectRatio="none"><polygon points="0,11 50,11 54,20 0,20" fill="var(--band-grey)"/><polygon points="55,0 100,0 100,20 60,20" fill="var(--brand-blue)"/></svg>
    <span class="wordmark wordmark--tone">NORVIX</span>
  </div>
</section>

<section class="piece envelope-front" aria-label="Envelope front">
  <div class="top-rule"></div>
  <span class="wordmark">NORVIX</span>
  <p class="return-address">If undelivered please return to:<br>22 PO Box 87, Lindale, Ohio 4512</p>
  <div class="footer-bands">
    <svg viewBox="0 0 100 20" preserveAspectRatio="none"><polygon points="0,11 50,11 54,20 0,20" fill="var(--band-grey)"/><polygon points="55,0 100,0 100,20 60,20" fill="var(--brand-blue)"/></svg>
    <span class="wordmark wordmark--tone">NORVIX</span>
  </div>
</section>

<section class="piece letterhead" aria-label="Letterhead">
  <div class="top-rule"></div>
  <span class="wordmark">NORVIX</span>
  <div class="header-contact">
    <b>NORVIX</b><br>22 PO Box 87, Lindale, Ohio 4512<br>Tel: 1300 262 818<br>Fax: 0409 316 207<br>info@norvix.com
  </div>
  <div class="header-rule"></div>
  <div class="letter-body">
    <p>May 14, 2024</p>
    <p>Alana Reyes<br>480 Harbor Lane<br>Lindale, OH 45120</p>
    <p>Dear Ms. Reyes,</p>
    <p>Thank you for meeting with our team last week to discuss the new border control platform.</p>
    <p>We have enclosed an outline of the identity, fingerprint and passport modules, along with a schedule for the pilot phase. Each module can be delivered on its own or as part of a complete turnkey system.</p>
    <p>Our engineers will be available on site throughout the rollout to support your staff and ensure every checkpoint runs smoothly from the first day.</p>
    <p>I would welcome the chance to talk through the details and answer any questions you may have.</p>
    <p>Regards,</p>
    <p>Evan Cole</p>
  </div>
  <div class="footer-bands">
    <svg viewBox="0 0 100 20" preserveAspectRatio="none"><polygon points="0,11 50,11 54,20 0,20" fill="var(--band-grey)"/><polygon points="55,0 100,0 100,20 60,20" fill="var(--brand-blue)"/></svg>
    <span class="wordmark wordmark--tone">NORVIX</span>
  </div>
</section>

<section class="piece card-back" aria-label="Business card back">
  <span class="wordmark">NORVIX</span>
</section>

<section class="piece card-front" aria-label="Business card front">
  <span class="wordmark">NORVIX</span>
  <div class="holder">
    <p class="holder-name">Daniel Harrow</p>
    <p class="holder-role">Manager</p>
  </div>
  <ul class="contact-list">
    <li><b>Address :</b> 22 PO Box 87, Lindale , Ohio 4512</li>
    <li><b>Email :</b> info@norvix.com</li>
    <li><b>Tel :</b> 1300 262 818</li>
    <li><b>Fax :</b> 0409 316 207</li>
  </ul>
  <div class="footer-bands">
    <svg viewBox="0 0 100 20" preserveAspectRatio="none"><polygon points="0,11 50,11 54,20 0,20" fill="var(--band-grey)"/><polygon points="55,0 100,0 100,20 60,20" fill="var(--brand-blue)"/></svg>
    <span class="wordmark wordmark--tone">NORVIX</span>
  </div>
</section>

</body>
</html>
```